Garden Design Flier

I would like a PDF of this half page A4 flier in soft green tones with dark green leaves.

Target Market(s)

Home owners and real estate agents

Font styles to use
Serif
Other font styles liked:
• Papyrus

Colors
acd136
9bcb3c
cadf82
fefdec

Requirements
Must have
• Green tones
Nice to have
• Leaves, vines, lawns
Should not have
• Open to ideas, but classic style

```html
<!DOCTYPE html>
<html lang="en">
<head>
<meta charset="utf-8">
<title>Harvest Beds – Garden Design Flier</title>
<link href="https://fonts.googleapis.com/css2?family=Lobster&family=Montserrat:wght@400;500;600&display=swap" rel="stylesheet">
<style>
  :root{
    --page-bg:#e4e4e4;
    --forest:#1f8a1c;
    --leaf:#2fa52a;
    --leaf-light:#4cbc33;
    --lime:#9bcb3c;
    --lime-soft:#acd136;
    --pale:#cadf82;
    --cream:#fefdec;
    --ink:#161616;
    --tick:#27402a;
    --phone:#6cc04a;
    --white:#ffffff;
  }
  *{box-sizing:border-box;margin:0;padding:0}
  html,body{width:725px;height:1200px;overflow:hidden}
  body{background:var(--page-bg);position:relative;font-family:"Montserrat",Arial,sans-serif;color:var(--ink)}

  .flier{position:absolute;left:79px;top:69px;width:568px;height:402px;background:var(--white);
    box-shadow:0 10px 18px rgba(0,0,0,.18);overflow:hidden}

  .foliage-header{position:absolute;left:0;top:0;width:100%;height:162px;
    background:radial-gradient(ellipse at 30% 40%,var(--leaf-light) 0%,var(--leaf) 45%,var(--forest) 100%)}

  .title-stripes{position:absolute;top:52px;width:35px;height:27px}
  .title-stripes.left{left:0}
  .title-stripes.right{right:0}

  .brand-name{position:absolute;left:0;right:0;top:12px;text-align:center;
    font-family:"Lobster",Georgia,serif;font-size:74px;line-height:1;color:var(--white)}

  .byline{position:absolute;left:46px;top:100px;color:var(--white);white-space:nowrap}
  .byline .owner{font-size:22px;font-weight:500}
  .byline .credential{font-size:13.5px;font-weight:500;margin-left:4px}

  .service-band{position:absolute;left:0;top:162px;width:100%;height:108px;background:var(--lime)}

  .steps{position:absolute;left:25px;top:149px;display:flex;gap:8px;list-style:none}
  .step{width:97px;height:27px;border-radius:9px;border:2px solid var(--cream);
    background:linear-gradient(#f3f7c9,var(--pale) 60%,var(--lime-soft));
    box-shadow:0 3px 4px rgba(0,0,0,.25);display:flex;align-items:center;justify-content:center;gap:4px;
    font-size:14px;font-weight:500;color:var(--tick)}
  .step svg{width:11px;height:11px}

  .benefits{position:absolute;top:183px;display:flex;gap:5px;font-size:13px;line-height:16px}
  .benefits svg{width:11px;height:11px;margin-top:2px;flex:none}
  .benefits.left{left:61px;width:200px}
  .benefits.right{left:288px;width:210px}

  .fence-border{position:absolute;left:0;top:270px;width:100%;height:48px;
    background:linear-gradient(var(--forest) 0%,var(--leaf) 40%,var(--white) 100%)}
  .leaf-sprig{position:absolute;left:55px;top:292px;width:135px;height:110px;border-radius:40% 60% 30% 50%;
    background:radial-gradient(ellipse,var(--leaf) 0%,rgba(47,165,42,.4) 55%,rgba(255,255,255,0) 75%)}

  .contact{position:absolute;left:201px;font-weight:500;display:flex;align-items:center}
  .contact svg{width:23px;height:19px;margin-right:17px}
  .contact.email{top:325px;font-size:14.5px}
  .contact.mobile{top:354px;font-size:14.5px}
  .contact.mobile svg{height:23px}
  .phone-number{font-size:33px;font-weight:600;color:var(--phone);margin-left:6px;letter-spacing:.5px}
</style>
</head>
<body>
  <article class="flier">
    <div class="foliage-header" role="img" aria-label="Lush green foliage texture background"></div>

    <svg class="title-stripes left" viewBox="0 0 35 27" aria-hidden="true">
      <rect y="0" width="35" height="4" fill="var(--pale)"/><rect y="11" width="35" height="4" fill="var(--pale)"/><rect y="22" width="35" height="4" fill="var(--pale)"/>
    </svg>
    <svg class="title-stripes right" viewBox="0 0 35 27" aria-hidden="true">
      <rect y="0" width="35" height="4" fill="var(--pale)"/><rect y="11" width="35" height="4" fill="var(--pale)"/><rect y="22" width="35" height="4" fill="var(--pale)"/>
    </svg>

    <h1 class="brand-name">Harvest Beds</h1>
    <p class="byline"><span class="owner">by Liam Hartwell</span><span class="credential">Certificate 3. Horticulture. Greenvale Institute</span></p>

    <div class="service-band"></div>

    <ul class="steps">
      <li class="step"><svg viewBox="0 0 12 12"><circle cx="6" cy="6" r="6" fill="var(--tick)"/><path d="M3.2 6.2l1.9 1.9 3.8-3.9" stroke="var(--pale)" stroke-width="1.6" fill="none"/></svg>DESIGN</li>
      <li class="step"><svg viewBox="0 0 12 12"><circle cx="6" cy="6" r="6" fill="var(--tick)"/><path d="M3.2 6.2l1.9 1.9 3.8-3.9" stroke="var(--pale)" stroke-width="1.6" fill="none"/></svg>INSTALL</li>
      <li class="step"><svg viewBox="0 0 12 12"><circle cx="6" cy="6" r="6" fill="var(--tick)"/><path d="M3.2 6.2l1.9 1.9 3.8-3.9" stroke="var(--pale)" stroke-width="1.6" fill="none"/></svg>GROW</li>
      <li class="step"><svg viewBox="0 0 12 12"><circle cx="6" cy="6" r="6" fill="var(--tick)"/><path d="M3.2 6.2l1.9 1.9 3.8-3.9" stroke="var(--pale)" stroke-width="1.6" fill="none"/></svg>TEND</li>
      <li class="step"><svg viewBox="0 0 12 12"><circle cx="6" cy="6" r="6" fill="var(--tick)"/><path d="M3.2 6.2l1.9 1.9 3.8-3.9" stroke="var(--pale)" stroke-width="1.6" fill="none"/></svg>ENJOY</li>
    </ul>

    <div class="benefits left">
      <svg viewBox="0 0 12 12"><circle cx="6" cy="6" r="6" fill="var(--ink)"/><path d="M3 6h5M6 3.5L8.5 6 6 8.5" stroke="var(--lime)" stroke-width="1.6" fill="none"/></svg>
      <p>All your gardening and landscaping needs from design and installation to general maintainance.</p>
    </div>
    <div class="benefits right">
      <svg viewBox="0 0 12 12"><circle cx="6" cy="6" r="6" fill="var(--ink)"/><path d="M3 6h5M6 3.5L8.5 6 6 8.5" stroke="var(--lime)" stroke-width="1.6" fill="none"/></svg>
      <p>Bespoke vegetable gardens and potager designs created to suite your site and requirements</p>
    </div>

    <div class="fence-border" role="img" aria-label="White picket fence beneath green foliage"></div>
    <div class="leaf-sprig" role="img" aria-label="Watercolour sprig of green leaves"></div>

    <p class="contact email">
      <svg viewBox="0 0 23 19" aria-hidden="true"><rect width="23" height="19" rx="2" fill="var(--phone)"/><path d="M2 4l9.5 7L21 4" stroke="var(--white)" stroke-width="2" fill="none"/></svg>
      Email : liam@harvestbeds.com.au
    </p>
    <p class="contact mobile">
      <svg viewBox="0 0 23 23" aria-hidden="true"><rect width="23" height="23" rx="3" fill="var(--phone)"/><path d="M7 5c-1.5 1-1.5 3 0 6s4 5 6.5 6c1.5.5 2.8-.3 3.3-1.5l-2.3-2.2-1.8 1c-1.6-.8-3.2-2.6-3.8-4l1.1-1.7L8 5.2z" fill="var(--white)"/></svg>
      Mobile:<span class="phone-number">0400-123456</span>
    </p>
  </article>
</body>
</html>
```